We are a Sydney based company looking for a Modern, Professional flyer design

We are a security company in Sydney and we need a flyer designed for our new sales campaign.

We need the flyer to be nice. clean and professional and to stand out.

We are currently running a new sales campaign that we need to get the customers attention. the campaign is that we will beat their current security bill or we will give them a $200 gift voucher. terms and conditions apply.

Target Market(s)

Local businesses

Industry/Entity Type

It Company

Requirements
Must have
• sales campaign details and offer
• - We will reduce your current security bill by 20% or receive a $200 gift voucher

```html
<!DOCTYPE html>
<html lang="en">
<head>
<meta charset="utf-8">
<title>Kestrel Services – Security Flyer</title>
<link rel="stylesheet" href="https://fonts.googleapis.com/css2?family=Oswald:wght@400;500;600&family=Open+Sans:wght@600;700&family=Libre+Baskerville:wght@400&display=swap">
<style>
  :root {
    --blue-deep: #1c3f8c;
    --blue-mid: #2f5bb4;
    --blue-light: #6f95d8;
    --blue-pale: #b9cbee;
    --navy-text: #1e2e5a;
    --grey-text: #3b3b3b;
    --paper: #f4f5f7;
    --white: #ffffff;
  }
  html, body {
    margin: 0;
    padding: 0;
    width: 692px;
    height: 1200px;
    overflow: hidden;
    background: var(--paper);
  }
  .flyer {
    position: relative;
    width: 692px;
    height: 1200px;
    overflow: hidden;
    background: linear-gradient(180deg, #fbfbfc 0%, #eceef2 100%);
    font-family: "Open Sans", Arial, sans-serif;
  }
  .hero-photo {
    position: absolute;
    left: 0; top: 0;
    width: 692px; height: 540px;
    background:
      radial-gradient(ellipse 60% 30% at 65% 62%, rgba(255,214,140,0.75) 0%, rgba(255,190,110,0.25) 45%, transparent 75%),
      linear-gradient(180deg, #2b5fb8 0%, #3e78cc 28%, #1d3f86 55%, #14264f 72%, #1a2d4e 100%);
  }
  .team-photo {
    position: absolute;
    left: 0; top: 520px;
    width: 692px; height: 560px;
    background:
      radial-gradient(ellipse 40% 55% at 62% 45%, rgba(150,150,155,0.28) 0%, transparent 70%),
      radial-gradient(ellipse 35% 50% at 18% 40%, rgba(160,160,165,0.22) 0%, transparent 70%),
      linear-gradient(180deg, #e9eaee 0%, #f3f4f6 100%);
  }
  .brand {
    position: absolute;
    left: 44px; top: 38px;
    display: flex;
    align-items: center;
    gap: 12px;
    padding: 14px 24px;
    background: var(--white);
    border-radius: 60px;
  }
  .brand-dot {
    width: 18px; height: 18px;
    border-radius: 50%;
    background: var(--blue-deep);
  }
  .brand-name {
    font-family: "Open Sans", Arial, sans-serif;
    font-weight: 700;
    font-size: 26px;
    color: var(--blue-deep);
    letter-spacing: 0.5px;
  }
  .waves {
    position: absolute;
    left: 0;
    width: 692px;
  }
  .waves--top { top: 420px; height: 160px; }
  .waves--bottom { top: 1040px; height: 160px; }
  .offer {
    position: absolute;
    left: 40px; top: 560px;
    width: 340px; height: 290px;
    box-sizing: border-box;
    padding: 16px 14px;
    display: flex;
    flex-direction: column;
    justify-content: center;
    align-items: center;
    background: var(--blue-deep);
    border: 4px solid var(--blue-light);
    border-radius: 14px;
    color: var(--white);
    text-align: center;
    font-family: "Oswald", "Arial Narrow", sans-serif;
    text-transform: uppercase;
    white-space: nowrap;
  }
  .offer-lead {
    margin: 0;
    font-family: "Open Sans", Arial, sans-serif;
    font-weight: 700;
    font-size: 18px;
    line-height: 1.3;
    letter-spacing: 0.3px;
  }
  .offer-figure {
    margin: 4px 0 0;
    font-weight: 500;
    font-size: 78px;
    line-height: 1;
  }
  .offer-alt {
    margin: 4px 0 0;
    font-weight: 500;
    font-size: 40px;
    line-height: 1.05;
  }
  .offer-voucher {
    margin: 2px 0 0;
    font-weight: 500;
    font-size: 30px;
    line-height: 1.15;
  }
  .services {
    position: absolute;
    left: 410px; top: 578px;
    margin: 0; padding: 0;
    list-style: none;
    width: 250px;
  }
  .services li {
    position: relative;
    padding-left: 24px;
    margin-bottom: 17px;
    font-weight: 700;
    font-size: 21px;
    line-height: 1.25;
    color: var(--navy-text);
  }
  .services li::before {
    content: "";
    position: absolute;
    left: 0; top: 8px;
    width: 11px; height: 11px;
    border-radius: 50%;
    background: var(--blue-mid);
  }
  .headline {
    position: absolute;
    left: 0; top: 895px;
    width: 692px;
    text-align: center;
    margin: 0;
  }
  .headline-top {
    display: block;
    font-family: "Libre Baskerville", Georgia, serif;
    font-weight: 400;
    font-size: 50px;
    color: var(--grey-text);
    letter-spacing: 1px;
    line-height: 1.1;
  }
  .headline-bottom {
    display: block;
    font-family: "Oswald", "Arial Narrow", sans-serif;
    font-weight: 500;
    font-size: 76px;
    color: var(--blue-deep);
    letter-spacing: 1px;
    line-height: 1.15;
  }
  .contact {
    position: absolute;
    left: 0; top: 1140px;
    width: 692px;
    display: flex;
    justify-content: space-between;
    box-sizing: border-box;
    padding: 0 50px;
    color: var(--white);
    font-weight: 600;
    font-size: 21px;
    white-space: nowrap;
  }
  .contact-item {
    display: flex;
    align-items: center;
    gap: 12px;
  }
  .contact-icon { width: 20px; height: 20px; }
</style>
</head>
<body>
<main class="flyer">
  <div class="hero-photo" role="img" aria-label="Sydney harbour skyline at dusk with lit opera house sails and harbour bridge"></div>
  <div class="team-photo" role="img" aria-label="Faded greyscale photo of business professionals in an office"></div>

  <svg class="waves waves--top" viewBox="0 0 692 160" preserveAspectRatio="none" aria-hidden="true">
    <path d="M0 20 C200 110 460 110 692 40 L692 160 L0 160 Z" fill="var(--blue-light)"/>
    <path d="M0 40 C200 120 460 120 692 60 L692 160 L0 160 Z" fill="var(--blue-deep)"/>
    <path d="M0 62 C210 135 470 135 692 80 L692 160 L0 160 Z" fill="var(--blue-pale)"/>
    <path d="M0 74 C210 148 470 148 692 94 L692 160 L0 160 Z" fill="#f1f2f5"/>
  </svg>

  <div class="brand">
    <span class="brand-dot"></span>
    <span class="brand-name">KESTREL Services</span>
  </div>

  <section class="offer">
    <p class="offer-lead">We will reduce your<br>current security bill</p>
    <p class="offer-figure">By 20%</p>
    <p class="offer-alt">Or receive a</p>
    <p class="offer-voucher">$200 gift voucher</p>
  </section>

  <ul class="services">
    <li>Control room</li>
    <li>Mobile patrols</li>
    <li>Static guarding</li>
    <li>Alarm monitoring</li>
    <li>CCTV and alarm installs</li>
    <li>Risk management</li>
  </ul>

  <h1 class="headline">
    <span class="headline-top">QUALITY SERVICE</span>
    <span class="headline-bottom">AT THE RIGHT PRICE</span>
  </h1>

  <svg class="waves waves--bottom" viewBox="0 0 692 160" preserveAspectRatio="none" aria-hidden="true">
    <path d="M0 70 C220 0 470 0 692 60 L692 160 L0 160 Z" fill="var(--blue-pale)"/>
    <path d="M0 82 C220 14 470 14 692 74 L692 160 L0 160 Z" fill="var(--blue-deep)"/>
    <path d="M0 94 C220 30 470 30 692 88 L692 160 L0 160 Z" fill="var(--blue-light)"/>
  </svg>

  <footer class="contact">
    <span class="contact-item">
      <svg class="contact-icon" viewBox="0 0 20 20" aria-hidden="true">
        <rect x="1" y="1" width="18" height="18" rx="3" fill="var(--white)"/>
        <path d="M6 5 L8 5 L9 8 L8 9 C9 11 10 12 12 13 L13 12 L16 13 L16 15 C11 16 5 10 6 5 Z" fill="var(--blue-light)"/>
      </svg>
      1300 22 4819
    </span>
    <span class="contact-item">
      <svg class="contact-icon" viewBox="0 0 20 20" aria-hidden="true">
        <rect x="1" y="4" width="18" height="12" rx="1.5" fill="var(--white)"/>
        <path d="M1.5 5 L10 11 L18.5 5" fill="none" stroke="var(--blue-light)" stroke-width="1.6"/>
      </svg>
      info@kestrel-services.com.au
    </span>
  </footer>
</main>
</body>
</html>
```